postcard for Real Estate Agent that sells homes for less than any other agents

My company sells houses for a fraction of what others charge. I have most of the verbiage but I am open to ideas.
Our post card will be 6.25 x 9
We need an image that goes with our words and draws people to take a look
We are playful at the same time very serious about the money we will save our clients. In the past our message has been received as too good to be true. Our old message was "save $6000* when you list with us" We think the "*" was causing people to think their was a catch. Other agents will tell people that we will not do what they will do and that is why they must charge more. We are a full service agency and we will generally do everything that other agents will do and in many cases we will do more than other agents. We are changing this industry and need our message to get to every person that is thinking of selling their home

Target Market(s)

People who want to list their home for sale

Industry/Entity Type

Real Estate Agent

Requirements
Must have
• Image that makes people read the message

```html
<!DOCTYPE html>
<html lang="en">
<head>
<meta charset="utf-8">
<title>Keystone Realty Postcard</title>
<link href="https://fonts.googleapis.com/css2?family=Open+Sans:wght@400;600;700;800&display=swap" rel="stylesheet">
<style>
  :root {
    --page: #e9e7e4;
    --navy: #0f2f66;
    --blue: #1d4f8f;
    --blue-light: #2a5c9c;
    --green: #76a943;
    --green-text: #8cc157;
    --ink: #3b3b3b;
    --grey: #555a60;
    --grey-light: #eceef1;
    --white: #ffffff;
    --photo-a: #d9dde3;
    --photo-b: #a9b9cf;
  }
  * { box-sizing: border-box; margin: 0; padding: 0; }
  html, body { width: 962px; height: 1200px; overflow: hidden; background: var(--page); }
  body { font-family: "Open Sans", Arial, sans-serif; }
  .stage { position: absolute; left: 0; top: 0; width: 870px; height: 1084px; transform: scale(1.1057, 1.107); transform-origin: 0 0; }
  .card { position: absolute; width: 648px; height: 450px; background: var(--white); box-shadow: 0 6px 16px rgba(0,0,0,.25); overflow: hidden; }
  .card--front { left: 76px; top: 67px; background: linear-gradient(90deg, #ffffff 0%, #ffffff 55%, #e3e6ea 100%); }
  .card--back { left: 148px; top: 569px; }
  .abs { position: absolute; }

  /* front */
  .front-header { left: 0; top: 0; width: 648px; height: 90px; }
  .kicker { left: 20px; top: 18px; font-size: 15px; font-weight: 700; color: var(--grey); letter-spacing: .2px; }
  .headline { left: 20px; top: 38px; font-size: 30px; font-weight: 700; color: var(--blue); }
  .blue-panel { left: 0; top: 0; }
  .intro { left: 28px; top: 118px; font-size: 13px; color: var(--green-text); line-height: 17px; }
  .intro b { font-weight: 700; }
  .intro::before { content: "\25B6"; position: absolute; left: -20px; top: 0; font-size: 11px; }
  .benefits { left: 28px; top: 167px; list-style: none; }
  .benefits li { position: relative; padding-left: 18px; font-size: 11.6px; line-height: 15.3px; color: var(--white); }
  .benefits li svg { position: absolute; left: 0; top: 4px; }
  .photo { left: 330px; top: 28px; width: 318px; height: 208px; background: radial-gradient(ellipse at 60% 55%, var(--photo-b), var(--photo-a) 70%, transparent 100%); }
  .offer-lead { left: 368px; top: 226px; font-size: 21px; font-weight: 700; color: var(--ink); }
  .offer-amount { left: 366px; top: 244px; font-size: 44px; font-weight: 800; color: var(--ink); letter-spacing: -.5px; }
  .offer-tail { left: 372px; top: 300px; font-size: 15px; font-weight: 700; color: var(--ink); }
  .band { background: var(--green); color: var(--white); font-weight: 700; }
  .band--front { left: 0; top: 333px; width: 648px; height: 32px; text-align: right; padding-right: 10px; font-size: 13px; line-height: 32px; letter-spacing: .4px; }
  .footer-front { left: 0; top: 365px; width: 648px; height: 85px; background: linear-gradient(90deg, #ffffff, var(--grey-light)); }
  .brand { display: flex; align-items: center; gap: 8px; font-size: 18px; font-weight: 800; color: var(--blue); }
  .brand-mark { width: 18px; height: 18px; background: var(--green); }
  .brand--front { left: 32px; top: 395px; }
  .tagline { font-size: 13px; font-weight: 700; color: var(--grey); white-space: nowrap; }
  .call { display: flex; align-items: center; gap: 6px; font-size: 16px; font-weight: 700; color: var(--blue); white-space: nowrap; }
  .tagline--front { left: 268px; top: 384px; }
  .call--front { left: 259px; top: 406px; }

  /* back */
  .brand--back { left: 26px; top: 48px; font-size: 22px; }
  .stamp { left: 548px; top: 18px; width: 72px; height: 52px; border: 1px solid #c9ccd0; }
  .address-line { left: 400px; width: 220px; height: 1px; background: #cfd2d6; }
  .back-art { left: 140px; top: 88px; width: 210px; height: 215px; background: radial-gradient(ellipse at 55% 40%, #c76b7e 0%, #7b6a96 35%, rgba(40,60,100,.6) 70%, transparent 100%); border-radius: 40% 40% 0 0; }
  .kicker--back { left: 14px; top: 170px; font-size: 12px; font-weight: 700; color: var(--white); letter-spacing: .4px; }
  .headline--back { left: 14px; top: 195px; font-size: 17px; font-weight: 700; color: var(--white); letter-spacing: .8px; }
  .subline { left: 14px; top: 227px; font-size: 11px; font-weight: 700; color: var(--white); line-height: 14px; letter-spacing: .3px; }
  .band--back { left: 0; top: 303px; width: 360px; height: 49px; text-align: center; font-size: 20px; line-height: 49px; letter-spacing: 1px; }
  .tagline--back { left: 38px; top: 370px; }
  .call--back { left: 30px; top: 394px; }
</style>
</head>
<body>
<main class="stage">

  <section class="card card--front" aria-label="Postcard front">
    <svg class="abs blue-panel" width="648" height="450" aria-hidden="true">
      <defs>
        <linearGradient id="panelFront" x1="0" y1="0" x2="1" y2="1">
          <stop offset="0" stop-color="#2a5c9c"/>
          <stop offset="1" stop-color="#0f2f66"/>
        </linearGradient>
      </defs>
      <polygon points="0,90 232,90 360,333 0,333" fill="url(#panelFront)"/>
    </svg>
    <p class="abs kicker">YOU’D HAVE TO BE</p>
    <h1 class="abs headline">Bat $#@T CRAZY!</h1>
    <p class="abs intro">Look at what you can do<br>with <b>$6000.00</b></p>
    <ul class="abs benefits">
      <li><svg width="10" height="8" viewBox="0 0 10 8"><path d="M1 4 L4 7 L9 1" stroke="#8cc157" stroke-width="1.6" fill="none"/></svg>Give it to your Kids</li>
      <li><svg width="10" height="8" viewBox="0 0 10 8"><path d="M1 4 L4 7 L9 1" stroke="#8cc157" stroke-width="1.6" fill="none"/></svg>Build a fence</li>
      <li><svg width="10" height="8" viewBox="0 0 10 8"><path d="M1 4 L4 7 L9 1" stroke="#8cc157" stroke-width="1.6" fill="none"/></svg>Build a deck</li>
      <li><svg width="10" height="8" viewBox="0 0 10 8"><path d="M1 4 L4 7 L9 1" stroke="#8cc157" stroke-width="1.6" fill="none"/></svg>Landscape</li>
      <li><svg width="10" height="8" viewBox="0 0 10 8"><path d="M1 4 L4 7 L9 1" stroke="#8cc157" stroke-width="1.6" fill="none"/></svg>Take a Vacation</li>
      <li><svg width="10" height="8" viewBox="0 0 10 8"><path d="M1 4 L4 7 L9 1" stroke="#8cc157" stroke-width="1.6" fill="none"/></svg>Buy new clothes</li>
      <li><svg width="10" height="8" viewBox="0 0 10 8"><path d="M1 4 L4 7 L9 1" stroke="#8cc157" stroke-width="1.6" fill="none"/></svg>Pay off your car</li>
      <li><svg width="10" height="8" viewBox="0 0 10 8"><path d="M1 4 L4 7 L9 1" stroke="#8cc157" stroke-width="1.6" fill="none"/></svg>Pay off student loan</li>
      <li><svg width="10" height="8" viewBox="0 0 10 8"><path d="M1 4 L4 7 L9 1" stroke="#8cc157" stroke-width="1.6" fill="none"/></svg>Buy New Carpet</li>
      <li><svg width="10" height="8" viewBox="0 0 10 8"><path d="M1 4 L4 7 L9 1" stroke="#8cc157" stroke-width="1.6" fill="none"/></svg>Upgrade Appliances</li>
    </ul>
    <div class="abs photo" role="img" aria-label="Photo of a man in a blue shirt shouting into a megaphone"></div>
    <p class="abs offer-lead">to give an agent</p>
    <p class="abs offer-amount">$6000.00</p>
    <p class="abs offer-tail">To put a sign in your yard</p>
    <div class="abs band band--front">www.KeystoneHomes.com</div>
    <div class="abs footer-front"></div>
    <div class="abs brand brand--front"><span class="brand-mark"></span>Keystone Realty</div>
    <p class="abs tagline tagline--front">Full Service Agency at a Fraction of the Cost</p>
    <p class="abs call call--front">Call Dale or Marcus at
      <svg width="16" height="16" viewBox="0 0 16 16" aria-hidden="true"><circle cx="8" cy="8" r="7" fill="none" stroke="#1d4f8f" stroke-width="1.4"/><path d="M5.2 4.5c.4-.3.9-.2 1.1.2l.6 1.2c.2.4 0 .7-.3 1l-.3.3c.4.9 1 1.5 1.9 1.9l.3-.3c.3-.3.6-.5 1-.3l1.2.6c.4.2.5.7.2 1.1-.6.8-1.6 1-2.5.5-1.7-.9-2.9-2.1-3.8-3.8-.5-.9-.3-1.9.6-2.4z" fill="#1d4f8f"/></svg>
      555.014.2290</p>
  </section>

  <section class="card card--back" aria-label="Postcard back">
    <svg class="abs blue-panel" width="648" height="450" aria-hidden="true">
      <defs>
        <linearGradient id="panelBack" x1="0" y1="0" x2="1" y2="1">
          <stop offset="0" stop-color="#2a5c9c"/>
          <stop offset="1" stop-color="#0f2f66"/>
        </linearGradient>
      </defs>
      <polygon points="0,132 300,132 360,250 360,303 0,303" fill="url(#panelBack)"/>
    </svg>
    <div class="abs brand brand--back"><span class="brand-mark"></span>Keystone Realty</div>
    <div class="abs stamp" aria-label="Stamp area"></div>
    <div class="abs address-line" style="top:186px"></div>
    <div class="abs address-line" style="top:211px"></div>
    <div class="abs address-line" style="top:235px"></div>
    <div class="abs address-line" style="top:260px"></div>
    <div class="abs address-line" style="top:285px"></div>
    <div class="abs back-art" role="img" aria-label="Photo of a thoughtful woman looking up at colourful speech bubbles with question and exclamation marks"></div>
    <p class="abs kicker--back">YOU’D HAVE TO BE</p>
    <h2 class="abs headline--back">Bat $#@T CRAZY</h2>
    <p class="abs subline">to give an agent $6000.00<br>To put a sign in your yard.</p>
    <div class="abs band band--back">www.KeystoneHomes.com</div>
    <p class="abs tagline tagline--back">Full Service Agency at a Fraction of the Cost</p>
    <p class="abs call call--back">Call Dale or Marcus at
      <svg width="16" height="16" viewBox="0 0 16 16" aria-hidden="true"><circle cx="8" cy="8" r="7" fill="none" stroke="#1d4f8f" stroke-width="1.4"/><path d="M5.2 4.5c.4-.3.9-.2 1.1.2l.6 1.2c.2.4 0 .7-.3 1l-.3.3c.4.9 1 1.5 1.9 1.9l.3-.3c.3-.3.6-.5 1-.3l1.2.6c.4.2.5.7.2 1.1-.6.8-1.6 1-2.5.5-1.7-.9-2.9-2.1-3.8-3.8-.5-.9-.3-1.9.6-2.4z" fill="#1d4f8f"/></svg>
      555.014.2290</p>
  </section>

</main>
</body>
</html>
```